Web design/Online store for an online apparel company

We need a website designed for an online apparel company called Birchwood Goods Co.. We need the categories for T-shirts, Tanks, Hoodies, and Headwear. Under T-shirts, we need the sub-categories of City/State Edition, Legendary Quotes, Logo, Nature, American, Christian, and Heritage Edition. We have a simple logo using the colors black, white, and gray/silver. We'd like the website to match. When using an accent color, use a shade of blue. The purpose of our company is to make apparel for people that is affordable, comfortable for any almost any occasion, and meaningful to the person wearing the clothing. Logo uploaded below.

```html
<!DOCTYPE html>
<html lang="en">
<head>
<meta charset="UTF-8">
<title>Birchwood Goods Co.</title>
<link rel="stylesheet" href="https://fonts.googleapis.com/css2?family=Poppins:wght@400;500;600;700;800&display=swap">
<style>
:root{
  --ink:#0b0b0c;
  --white:#ffffff;
  --promo:#4a5370;
  --band:#eff0f0;
  --card:#f1f1f1;
  --muted:#8e8c91;
  --title-gray:#7a777c;
  --label:#a3a3a3;
  --dot-1:#1f2a4a;
  --dot-2:#4a5f95;
  --dot-3:#d8e1f0;
  --dot-4:#d9a520;
}
*{box-sizing:border-box;margin:0;padding:0}
html,body{width:1200px;height:3174px;overflow:hidden;background:var(--white)}
body{position:relative;font-family:'Poppins',sans-serif;color:var(--ink)}
.abs{position:absolute}
.promo{left:0;top:0;width:1200px;height:30px;background:var(--promo);color:var(--white);font-size:14px;text-align:center;line-height:30px}
.promo .close{position:absolute;right:14px;top:9px}
.nav{left:0;top:30px;width:1200px;height:113px;background:var(--ink)}
.nav a{position:absolute;top:48px;color:var(--white);font-weight:600;font-size:16px;text-decoration:none;letter-spacing:.2px}
.nav .brand{position:absolute;left:510px;width:180px;top:46px;text-align:center;color:var(--white);font-size:15px;font-weight:600;white-space:nowrap}
.nav svg{position:absolute;top:46px}
.hero{left:0;top:143px;width:1200px;height:464px;background:#ebebeb}
.hero-photo{left:560px;top:143px;width:640px;height:507px;background:linear-gradient(135deg,#f2f2f2 0%,#a9c6e8 45%,#e8e2d4 75%,#dcdcdc 100%)}
.hero-title{left:111px;top:265px;font-size:54px;font-weight:800;line-height:68px;color:var(--title-gray);letter-spacing:.5px}
.btn{display:block;text-align:center;border-radius:30px;font-weight:600;color:var(--white)}
.btn-dark{left:111px;top:425px;width:164px;height:58px;line-height:58px;background:var(--ink);font-size:17px}
.arrow{width:40px;height:40px}
.section-title{font-size:46px;font-weight:800;letter-spacing:.3px}
.card{width:230px;height:307px;background:var(--card);border-radius:6px}
.card-fill{position:absolute;left:20px;top:30px;right:20px;bottom:30px;border-radius:4px}
.p-label{font-size:14px;font-weight:600;color:var(--label)}
.p-desc{font-size:16px;font-weight:500;line-height:21px;width:230px}
.dots span{display:inline-block;width:9px;height:9px;border-radius:50%;margin-right:10px}
.price{font-size:15px;width:60px;text-align:right}
.cats{left:0;top:1339px;width:1200px;height:371px;background:var(--band)}
.cat-circle{width:124px;height:124px;border-radius:50%;box-shadow:0 4px 10px rgba(0,0,0,.18)}
.cat-name{width:200px;text-align:center;font-size:17px;font-weight:600}
.about{left:0;top:1710px;width:1200px;height:490px;background:var(--ink)}
.about-photo{left:111px;top:1758px;width:403px;height:408px;background:linear-gradient(160deg,#b39067 0%,#8c6f4f 40%,#ebe9e3 70%,#d8d4cc 100%)}
.about-title{left:625px;top:1788px;color:var(--white);font-size:46px;font-weight:800}
.about-copy{left:625px;top:1857px;width:480px}
.about-copy p{color:var(--white);font-size:15.5px;line-height:28.5px;white-space:nowrap}
.about-copy p + p{margin-top:16px}
.btn-gray{background:var(--muted);font-size:17px}
.tee-name{font-size:15px;font-weight:600}
.tee-sub{font-size:15px;font-weight:600;color:var(--muted)}
.footer{left:0;top:2853px;width:1200px;height:321px;background:var(--ink);color:var(--white)}
.f-link{font-size:15px;font-weight:600;color:var(--white)}
.f-text{font-size:15px;font-weight:600;color:var(--white)}
.input{left:846px;top:2958px;width:242px;height:58px;border-radius:30px;background:var(--white);color:var(--ink);font-size:14px;line-height:58px;padding-left:35px}
.copy{left:0;width:1200px;top:3102px;text-align:center;color:var(--white);font-size:13px;font-weight:500}
</style>
</head>
<body>

<div class="abs promo">20% off everything from 29$!
  <svg class="close" width="12" height="12" viewBox="0 0 12 12"><path d="M1 1l10 10M11 1L1 11" stroke="#fff" stroke-width="1.5"/></svg>
</div>

<header class="abs nav">
  <svg style="left:110px" width="22" height="22" viewBox="0 0 22 22" fill="none" stroke="#fff" stroke-width="2"><circle cx="9" cy="9" r="7"/><path d="M14 14l6 6"/></svg>
  <a style="left:192px">HOME</a>
  <a style="left:282px">PRODUCT</a>
  <a style="left:399px">CATEGORIES</a>
  <div class="brand">Birchwood Goods Co.</div>
  <a style="left:709px">ABOUT</a>
  <a style="left:806px">CONTACT</a>
  <svg style="left:961px" width="22" height="24" viewBox="0 0 22 24" fill="none" stroke="#fff" stroke-width="2"><path d="M11 22s8-7 8-13a8 8 0 0 0-16 0c0 6 8 13 8 13z"/><circle cx="11" cy="9" r="3"/></svg>
  <svg style="left:1015px" width="22" height="24" viewBox="0 0 22 24" fill="none" stroke="#fff" stroke-width="2"><circle cx="11" cy="7" r="5"/><path d="M2 22c0-6 4-8 9-8s9 2 9 8z"/></svg>
  <svg style="left:1069px" width="22" height="24" viewBox="0 0 22 24" fill="none" stroke="#fff" stroke-width="2"><path d="M3 7h16l-1 15H4z"/><path d="M7 10V5a4 4 0 0 1 8 0v5"/></svg>
</header>

<section class="abs hero"></section>
<div class="abs hero-photo" role="img" aria-label="Model in a light blue hooded dress and cream boots seated on a white chair"></div>
<h1 class="abs hero-title">WELCOME TO<br>BIRCHWOOD GOODS CO.</h1>
<a class="abs btn btn-dark">SHOP NOW</a>
<svg class="abs arrow" style="left:35px;top:352px" viewBox="0 0 40 40" fill="none"><circle cx="20" cy="20" r="19" stroke="#b5b5b5" stroke-width="2"/><path d="M23 13l-7 7 7 7" stroke="#b5b5b5" stroke-width="2"/></svg>
<svg class="abs arrow" style="left:1123px;top:352px" viewBox="0 0 40 40" fill="none"><circle cx="20" cy="20" r="19" stroke="#0b0b0c" stroke-width="2"/><path d="M17 13l7 7-7 7" stroke="#0b0b0c" stroke-width="2"/></svg>

<h2 class="abs section-title" style="left:111px;top:684px">FEATURED PRODUCTS</h2>

<div class="abs card" style="left:111px;top:788px"><div class="card-fill" role="img" aria-label="Black crew-neck t-shirt" style="background:radial-gradient(circle,#151515 45%,#f1f1f1 70%)"></div></div>
<div class="abs card" style="left:360px;top:788px"><div class="card-fill" role="img" aria-label="Black racerback tank top" style="background:radial-gradient(ellipse 35% 50%,#1b1b1b 60%,#f1f1f1 100%)"></div></div>
<div class="abs card" style="left:609px;top:788px"><div class="card-fill" role="img" aria-label="Yellow pullover hoodie" style="background:radial-gradient(circle,#f0b416 50%,#f1f1f1 72%)"></div></div>
<div class="abs card" style="left:858px;top:788px"><div class="card-fill" role="img" aria-label="Red pullover hoodie" style="background:radial-gradient(circle,#d42424 50%,#f1f1f1 72%)"></div></div>

<div class="abs p-label" style="left:111px;top:1120px">LOREM IPSUM</div>
<div class="abs p-label" style="left:360px;top:1120px">LOREM IPSUM</div>
<div class="abs p-label" style="left:609px;top:1120px">LOREM IPSUM</div>
<div class="abs p-label" style="left:858px;top:1120px">LOREM IPSUM</div>
<div class="abs p-desc" style="left:111px;top:1159px">Lorem ipsum dolor siamet, consectetur adipiscing.</div>
<div class="abs p-desc" style="left:360px;top:1159px">Lorem ipsum dolor siamet, consectetur adipiscing.</div>
<div class="abs p-desc" style="left:609px;top:1159px">Lorem ipsum dolor siamet, consectetur adipiscing.</div>
<div class="abs p-desc" style="left:858px;top:1159px">Lorem ipsum dolor siamet, consectetur adipiscing.</div>

<div class="abs dots" style="left:111px;top:1239px"><span style="background:var(--dot-1)"></span><span style="background:var(--dot-2)"></span><span style="background:var(--dot-3)"></span><span style="background:var(--dot-4)"></span></div>
<div class="abs dots" style="left:360px;top:1239px"><span style="background:var(--dot-1)"></span><span style="background:var(--dot-2)"></span><span style="background:var(--dot-3)"></span><span style="background:var(--dot-4)"></span></div>
<div class="abs dots" style="left:609px;top:1239px"><span style="background:var(--dot-1)"></span><span style="background:var(--dot-2)"></span><span style="background:var(--dot-3)"></span><span style="background:var(--dot-4)"></span></div>
<div class="abs dots" style="left:858px;top:1239px"><span style="background:var(--dot-1)"></span><span style="background:var(--dot-2)"></span><span style="background:var(--dot-3)"></span><span style="background:var(--dot-4)"></span></div>
<div class="abs price" style="left:264px;top:1233px">$250</div>
<div class="abs price" style="left:513px;top:1233px">$250</div>
<div class="abs price" style="left:762px;top:1233px">$250</div>
<div class="abs price" style="left:1011px;top:1233px">$250</div>

<section class="abs cats"></section>
<h2 class="abs section-title" style="left:0;width:1200px;text-align:center;top:1392px">PRODUCT CATEGORIES</h2>
<div class="abs cat-circle" style="left:209px;top:1487px;background:linear-gradient(160deg,#8a6a55,#f4f4f4)" role="img" aria-label="Woman in a white t-shirt"></div>
<div class="abs cat-circle" style="left:427px;top:1487px;background:linear-gradient(160deg,#e8dccb,#c99a78)" role="img" aria-label="Man in a white tank top holding a basketball"></div>
<div class="abs cat-circle" style="left:646px;top:1487px;background:linear-gradient(160deg,#6b7f8c,#141414)" role="img" aria-label="Man in a black hoodie and cap"></div>
<div class="abs cat-circle" style="left:866px;top:1487px;background:linear-gradient(160deg,#9fc6dc,#3f75a8)" role="img" aria-label="Man in a white hat and sunglasses by the sea"></div>
<div class="abs cat-name" style="left:171px;top:1632px">T-SHIRTS</div>
<div class="abs cat-name" style="left:389px;top:1632px">TANKS</div>
<div class="abs cat-name" style="left:608px;top:1632px">HOODIES</div>
<div class="abs cat-name" style="left:828px;top:1632px">HEADWEAR</div>

<section class="abs about"></section>
<div class="abs about-photo" role="img" aria-label="Two friends in white hoodies laughing against a rock wall"></div>
<h2 class="abs about-title">ABOUT US</h2>
<div class="abs about-copy">
  <p>Lorem ipsum dolor sit amet, consectetur adipiscing elit,<br>sed do eiusmod tempor incididunt ut labdolore magna<br>aliqua. Quis ipsum suspendisse ultrica. Risus commodo<br>viverra maecenas accumsan lacus vel facilisis.</p>
  <p>Quis ipsum suspendisse ultrica. Risus commodo viverd<br>ra maecenas accumsan lacus vel facilisis.</p>
</div>
<a class="abs btn btn-gray" style="left:625px;top:2070px;width:163px;height:58px;line-height:58px">SHOP NOW</a>

<h2 class="abs section-title" style="left:111px;top:2264px">T-SHIRTS</h2>
<div class="abs card" style="left:111px;top:2368px"><div class="card-fill" role="img" aria-label="Black t-shirt with a colourful city print" style="background:radial-gradient(circle,#151515 45%,#f1f1f1 70%)"></div></div>
<div class="abs card" style="left:360px;top:2368px"><div class="card-fill" role="img" aria-label="Black t-shirt with a motivational quote print" style="background:radial-gradient(circle,#1a1a1a 45%,#f1f1f1 70%)"></div></div>
<div class="abs card" style="left:609px;top:2368px"><div class="card-fill" role="img" aria-label="Black t-shirt with a sunset forest print" style="background:radial-gradient(circle,#d0622a 12%,#1a1a1a 20%,#1a1a1a 45%,#f1f1f1 70%)"></div></div>
<div class="abs card" style="left:858px;top:2368px"><div class="card-fill" role="img" aria-label="Black t-shirt with a flag print" style="background:radial-gradient(circle,#2a3a78 10%,#1a1a1a 20%,#1a1a1a 45%,#f1f1f1 70%)"></div></div>
<svg class="abs arrow" style="left:34px;top:2501px" viewBox="0 0 40 40" fill="none"><circle cx="20" cy="20" r="19" stroke="#b5b5b5" stroke-width="2"/><path d="M23 13l-7 7 7 7" stroke="#b5b5b5" stroke-width="2"/></svg>
<svg class="abs arrow" style="left:1123px;top:2501px" viewBox="0 0 40 40" fill="none"><circle cx="20" cy="20" r="19" stroke="#0b0b0c" stroke-width="2"/><path d="M17 13l7 7-7 7" stroke="#0b0b0c" stroke-width="2"/></svg>
<div class="abs tee-name" style="left:111px;top:2706px">CITY/STATE EDITION</div>
<div class="abs tee-name" style="left:360px;top:2706px">LEGENDARY QUOTES</div>
<div class="abs tee-name" style="left:609px;top:2706px">NATURE</div>
<div class="abs tee-name" style="left:858px;top:2706px">AMERICAN</div>
<div class="abs tee-sub" style="left:111px;top:2733px">Lorem ipsum dolor.</div>
<div class="abs tee-sub" style="left:360px;top:2733px">Lorem ipsum dolor.</div>
<div class="abs tee-sub" style="left:609px;top:2733px">Lorem ipsum dolor.</div>
<div class="abs tee-sub" style="left:858px;top:2733px">Lorem ipsum dolor.</div>

<footer class="abs footer"></footer>
<div class="abs f-text" style="left:111px;top:2975px;font-size:17px">Birchwood Goods Co.</div>
<div class="abs f-link" style="left:333px;top:2912px">HOME</div>
<div class="abs f-link" style="left:333px;top:2940px">PRODUCT</div>
<div class="abs f-link" style="left:333px;top:2968px">GOODIES</div>
<div class="abs f-link" style="left:333px;top:2996px">ABOUT</div>
<div class="abs f-link" style="left:333px;top:3024px">CONTACT</div>
<svg class="abs" style="left:489px;top:2914px" width="16" height="20" viewBox="0 0 16 20"><path d="M8 19s7-6 7-11A7 7 0 0 0 1 8c0 5 7 11 7 11z" fill="#fff"/><circle cx="8" cy="8" r="2.5" fill="#0b0b0c"/></svg>
<div class="abs f-text" style="left:519px;top:2917px">BIRCHWOOD GOODS CO.,</div>
<div class="abs f-text" style="left:519px;top:2949px">ADDRESS COMES HERE</div>
<svg class="abs" style="left:487px;top:2982px" width="19" height="19" viewBox="0 0 24 24"><path d="M6.6 10.8a15 15 0 0 0 6.6 6.6l2.2-2.2c.3-.3.7-.4 1-.2 1.1.4 2.3.6 3.6.6.6 0 1 .4 1 1V20c0 .6-.4 1-1 1A17 17 0 0 1 3 4c0-.6.4-1 1-1h3.5c.6 0 1 .4 1 1 0 1.3.2 2.5.6 3.6.1.3 0 .7-.2 1z" fill="#fff"/></svg>
<div class="abs f-text" style="left:519px;top:2982px">+1 555-014-2290</div>
<svg class="abs" style="left:487px;top:3018px" width="19" height="14" viewBox="0 0 19 14"><rect width="19" height="14" rx="1" fill="#fff"/><path d="M1 1l8.5 7L18 1" stroke="#0b0b0c" stroke-width="1.5" fill="none"/></svg>
<div class="abs f-text" style="left:519px;top:3014px;font-size:14px">HELLO@BIRCHWOODGOODS.EXAMPLE</div>
<div class="abs f-text" style="left:846px;top:2912px">SUBSCRIBE NEWSLETTER</div>
<div class="abs input">Email Address</div>
<a class="abs btn btn-gray" style="left:846px;top:3028px;width:135px;height:58px;line-height:58px">SUBMIT</a>
<div class="abs copy">2024 BIRCHWOOD GOODS CO. ALL RIGHTS RESERVED.</div>

</body>
</html>
```